Bramwell Garden Maintenance - Needs a business card! Easy JOB!

I need a business card for a new company called Bramwell Garden Maintenance. I will be offering the below services.

I am relatively open for ideas, so please be at your creative best.

I think I will list all the services offered on the rear of the card.

- Gardening
- Lawn Care
- Hedge Trimming
- Rubbish Removal
- Weeding/Spraying
- Landscaping
- Gutter Cleaning
- Solar Panel Cleaning
- Irrigation
- Pruning
- On-Site Mulching
- Ask for other services

I am still a little undecided on the colours. I prefer the logos with the Blue text, but I am open for ideas ( the logo/texts colours are not final).

Please use the catch phrase "What can Bramwell do for you?"

Here are the required details.

Bramwell Garden Maintenance

Neil Harcourt (owner)
Ph: 1300 XXX XXX
Mob: 0427 XXX XXX

neil@bramwellgarden.com.au
www.bramwellgarden.com.au
facebook.com/BramwellGarden
twitter.com/BramwellGarden
ABN: XXX XXX XXX ( this can be in smaller text somewhere, this is the least important )

Thankyou in advance! And good luck.

regards,
Neil
Updates

Hi everyone, please make sure you include the phrase "What can Bramwell do for you?" on the designs.

thanks,
Neil

Definitely liking the focus on a majority of the design on the blue colour from the logo. Also a splash of green in the plant.

Please make sure you list the services provided on the rear of the card. thanks.

With the service listing, please make "ask for other services" stand out, either a different colour or position or size... as long as it is more noticeable than the other services listed. Thanks.

Industry/Entity Type

Business

Requirements
Must have
• - use the font supplied (Brandon Family Font)
- use of the catch phrase "What can Bramwell do for you?"
- Double sided design
- Facebook and Twitter logos/links
- Please use symbol/picture for "phone" "mobile" "email" instead of using the words.
- List the services provided on the rear of the card

```html
<!DOCTYPE html>
<html lang="en">
<head>
<meta charset="utf-8">
<title>Bramwell Garden Maintenance – Services</title>
<link rel="stylesheet" href="https://fonts.googleapis.com/css2?family=Fredoka:wght@500&family=Cabin:wght@400&display=swap">
<style>
  :root {
    --paper: #ffffff;
    --lime: #b2f400;
    --leaf-green: #5fe000;
    --service-grey: #5e6366;
    --service-edge: #6b7073;
    --accent-green: #2f8a16;
  }
  * { margin: 0; padding: 0; box-sizing: border-box; }
  html, body {
    width: 1200px;
    height: 686px;
    overflow: hidden;
    background: var(--paper);
  }
  .card-back {
    position: relative;
    width: 1200px;
    height: 686px;
    background: var(--paper);
    overflow: hidden;
  }
  .header-wave {
    position: absolute;
    inset: 0 0 auto 0;
    width: 1200px;
    height: 260px;
  }
  .service-list {
    position: absolute;
    list-style: none;
    font-family: "Fredoka", "Varela Round", sans-serif;
    font-weight: 500;
    font-size: 39px;
    line-height: 56px;
    color: var(--service-grey);
    -webkit-text-stroke: 5px var(--paper);
    paint-order: stroke fill;
    text-shadow:
      2px 0 0 var(--service-edge), -2px 0 0 var(--service-edge),
      0 2px 0 var(--service-edge), 0 -2px 0 var(--service-edge),
      2px 2px 0 var(--service-edge), -2px -2px 0 var(--service-edge),
      2px -2px 0 var(--service-edge), -2px 2px 0 var(--service-edge),
      2px 4px 3px rgba(0,0,0,0.35);
    letter-spacing: -0.3px;
    white-space: nowrap;
  }
  .service-list--garden { left: 120px; top: 240px; }
  .service-list--property { left: 709px; top: 267px; }
  .other-services {
    position: absolute;
    left: 0;
    width: 1162px;
    top: 578px;
    text-align: center;
    font-family: "Cabin", "Lato", sans-serif;
    font-weight: 400;
    font-size: 41px;
    color: var(--accent-green);
    letter-spacing: -0.3px;
  }
</style>
</head>
<body>
<main class="card-back">
  <svg class="header-wave" viewBox="0 0 1200 260" aria-hidden="true">
    <path fill="var(--lime)" d="M0,0 H1200 V140 C1110,185 960,222 770,212 C620,204 590,160 470,95 C350,30 150,60 0,232 Z"/>
    <path fill="var(--leaf-green)" d="M0,222 C90,110 270,40 480,66 C300,52 140,112 0,190 Z"/>
    <path fill="none" stroke="var(--leaf-green)" stroke-width="4" stroke-linecap="round" d="M560,82 C700,150 860,165 1085,112"/>
    <circle cx="1152" cy="62" r="62" fill="none" stroke="var(--leaf-green)" stroke-width="22"/>
  </svg>

  <ul class="service-list service-list--garden">
    <li>Gardening</li>
    <li>- Lawn Care</li>
    <li>- Hedge Trimming</li>
    <li>- Rubbish Removal</li>
    <li>- Weeding/Spraying</li>
    <li>- Landscaping</li>
  </ul>

  <ul class="service-list service-list--property">
    <li>Gutter Cleaning</li>
    <li>- Solar Panel Cleaning</li>
    <li>- Irrigation</li>
    <li>- Pruning</li>
    <li>- On-Site Mulching</li>
  </ul>

  <p class="other-services">Ask for other services</p>
</main>
</body>
</html>
```